indépendant en tant que Massothérapeute et Préparateur Mental, j'ai besoin de ...

Massothérapeute et préparateur mental indépendant, je recherche une carte de visite sobre et dynamique, sans images liées au massage ou à la préparation mentale mais intégrant mon logo. Les couleurs que j'aime bien sont : Blanc, gris, anthracite, noir et jaune

Contact Information for Business Card

carte de préférence Horizontale
neutre qui puisse toucher le deux domaines Massothérapie et préparation mentale

Requirements
Must have
• mon projet doit intégrer au recto:
LOGO
Loïc Vermande
078 315 26 49
info@loicvermande-exemple.ch
et éventuellement www.loicvermande-exemple.ch

et au verso les deux adresses:

Chemin des Ormelets 27B
1400 Yverdon-les-Bains

Rue des Tanneries 9
1700 Fribourg

Should not have
• mon projet ne doit pas contenir d'image en liens avec le massage ni la préparation mentale.

```html
<!DOCTYPE html>
<html lang="fr">
<head>
<meta charset="utf-8">
<title>Loïc Vermande – Cartes de visite</title>
<link rel="stylesheet" href="https://fonts.googleapis.com/css2?family=Roboto:wght@400;500&display=swap">
<style>
  :root {
    --backdrop: #8a8a8a;
    --paper: #ffffff;
    --anthracite: #231f20;
    --ink: #1e1e1e;
    --ink-soft: #4a4a4a;
    --silver: #b3a9ad;
    --silver-dim: #3a3537;
  }
  * { box-sizing: border-box; margin: 0; padding: 0; }
  html, body { width: 1200px; height: 1200px; overflow: hidden; }
  body {
    background: var(--backdrop);
    font-family: "Roboto", Arial, sans-serif;
    position: relative;
  }
  .card {
    position: absolute;
    left: 262px;
    width: 686px;
    height: 380px;
  }
  .card--front { top: 165px; background: var(--paper); }
  .card--back { top: 653px; height: 391px; background: var(--anthracite); }

  .brand {
    position: absolute;
    display: flex;
    align-items: center;
    gap: 12px;
  }
  .brand__dot {
    width: 30px; height: 30px; border-radius: 50%;
    flex: none;
  }
  .brand__name {
    font-weight: 500;
    letter-spacing: 0.5px;
    line-height: 1;
  }
  .brand__tagline {
    font-weight: 400;
    text-transform: uppercase;
    letter-spacing: 0.6px;
    margin-top: 5px;
  }

  .card--front .brand { left: 52px; top: 174px; }
  .card--front .brand__dot { background: var(--ink); }
  .card--front .brand__name { font-size: 22px; color: var(--ink); }
  .card--front .brand__tagline { font-size: 7.5px; color: var(--ink); }

  .divider {
    position: absolute;
    left: 379px; top: 100px;
    width: 2px; height: 190px;
    background: var(--ink);
  }
  .contact {
    position: absolute;
    left: 400px; top: 100px;
    color: var(--ink-soft);
    font-size: 15.5px;
    line-height: 19px;
  }
  .contact__name {
    font-size: 22px;
    font-weight: 500;
    color: var(--ink);
    margin-bottom: 17px;
    line-height: 26px;
  }
  .contact__address { padding-left: 3px; margin-bottom: 6px; }
  .contact__lines { list-style: none; margin-top: 8px; padding-left: 3px; }
  .contact__lines li { display: flex; align-items: center; gap: 10px; }
  .contact__lines svg { width: 12px; height: 12px; fill: var(--ink); flex: none; }

  .card--back .brand { left: 94px; top: 170px; gap: 16px; }
  .card--back .brand__dot { width: 44px; height: 44px; background: var(--silver); }
  .card--back .brand__name { font-size: 32px; color: var(--silver); }
  .card--back .brand__tagline { font-size: 10px; color: var(--silver-dim); margin-top: 7px; letter-spacing: 1px; }
</style>
</head>
<body>

<section class="card card--front" aria-label="Recto">
  <div class="brand">
    <span class="brand__dot"></span>
    <div>
      <div class="brand__name">Loïc Vermande</div>
      <div class="brand__tagline">Massothérapeute / Préparateur Mental</div>
    </div>
  </div>

  <div class="divider"></div>

  <div class="contact">
    <h1 class="contact__name">Loïc Vermande</h1>
    <p class="contact__address">Chemin des Ormelets 27B<br>1400 Yverdon-les-Bain</p>
    <p class="contact__address">Rue des Tanneries 9<br>1700 Fribourg</p>
    <ul class="contact__lines">
      <li>
        <svg viewBox="0 0 24 24" aria-hidden="true"><path d="M6.6 10.8a15.1 15.1 0 0 0 6.6 6.6l2.2-2.2c.3-.3.7-.4 1-.2 1.1.4 2.3.6 3.6.6.6 0 1 .4 1 1V20c0 .6-.4 1-1 1C10.6 21 3 13.4 3 4c0-.6.4-1 1-1h3.5c.6 0 1 .4 1 1 0 1.3.2 2.5.6 3.6.1.3 0 .7-.2 1z"/></svg>
        078 315 26 49
      </li>
      <li>
        <svg viewBox="0 0 24 24" aria-hidden="true"><path d="M2 5h20v14H2z M3 6l9 7 9-7" fill="none" stroke="#1e1e1e" stroke-width="0"/><path d="M2 5h20v2l-10 7L2 7zM2 9l10 7 10-7v10H2z"/></svg>
        info@loicvermande-exemple.ch
      </li>
      <li>
        <svg viewBox="0 0 24 24" aria-hidden="true"><circle cx="12" cy="12" r="10"/><path d="M7 8c2 0 3 1 3 3s-2 2-2 4M15 5c-1 2 0 3 2 3s2 3 1 5" stroke="#fff" stroke-width="1.6" fill="none"/></svg>
        www.loicvermande-exemple.ch
      </li>
    </ul>
  </div>
</section>

<section class="card card--back" aria-label="Verso">
  <div class="brand">
    <span class="brand__dot"></span>
    <div>
      <div class="brand__name">Loïc Vermande</div>
      <div class="brand__tagline">Massothérapeute / Préparateur Mental</div>
    </div>
  </div>
</section>

</body>
</html>
```